Redesign of an insurance website

Attached is an insurance website that I need to redesign. Currently the website is too dark. I like for example www.brenvalo.com . Could you make the website lighter and change the structure a little so that it is more user friendly?

Industry/Entity Type

Insurance

Number of Pages Required

4 page

```html
<!DOCTYPE html>
<html lang="cs">
<head>
<meta charset="utf-8">
<title>Kestrava – Indulge. Infer. Insure.</title>
<link rel="stylesheet" href="https://fonts.googleapis.com/css2?family=PT+Sans:wght@400;700&family=Lato:wght@300;400&display=swap">
<style>
  :root{
    --sky-top:#7c7a86;
    --sky-mid:#a08c92;
    --sunset:#c79a82;
    --horizon:#9a8a8c;
    --sea:#4d6577;
    --sea-deep:#3f586c;
    --white:#ffffff;
    --white-soft:rgba(255,255,255,.62);
    --label:#9aa0a8;
    --field-text:#222832;
    --divider:#d9dde2;
    --cta:#2b86f7;
  }
  *{margin:0;padding:0;box-sizing:border-box}
  html,body{width:1200px;height:619px;overflow:hidden}
  body{font-family:"PT Sans",sans-serif;color:var(--white);position:relative}
  .hero-backdrop{
    position:absolute;inset:0;
    background:linear-gradient(180deg,var(--sky-top) 0%,var(--sky-mid) 30%,var(--sunset) 50%,var(--horizon) 60%,var(--sea) 72%,var(--sea-deep) 100%);
  }
  .site-header{position:absolute;top:0;left:0;right:0;height:80px}
  .brand{position:absolute;left:26px;top:27px;font-family:"PT Sans",sans-serif;font-weight:400;font-size:21px;letter-spacing:.3px;color:var(--white)}
  .login-link{position:absolute;right:28px;top:21px;font-size:17px;color:var(--white);text-decoration:none}
  .headline{position:absolute;top:170px;left:0;right:0;text-align:center;font-weight:400;font-size:55px;letter-spacing:.5px}
  .product-carousel{position:absolute;top:258px;left:0;right:0;height:100px}
  .carousel-arrow{position:absolute;top:30px}
  .carousel-arrow.prev{left:380px}
  .carousel-arrow.next{left:801px}
  .product{position:absolute;text-align:center;font-family:"Lato",sans-serif;font-weight:400}
  .product svg{display:block;margin:0 auto}
  .product.accident{left:440px;width:80px;top:22px;color:var(--white-soft);font-size:15.5px}
  .product.flight{left:535px;width:130px;top:4px;color:var(--white);font-size:16px}
  .product.business{left:680px;width:80px;top:24px;color:var(--white-soft);font-size:15.5px}
  .product span{display:block;margin-top:4px}
  .quote-form{position:absolute;left:225px;top:386px;width:750px;height:56px;background:var(--white);border-radius:5px;display:flex;overflow:hidden}
  .field{position:relative;padding:16px 0 0 11px;font-family:"Lato",sans-serif}
  .field+.field::before{content:"";position:absolute;left:0;top:18px;height:23px;width:1px;background:var(--divider)}
  .field.first{width:187px;padding-left:37px}
  .field.last{width:189px}
  .field.email{flex:1}
  .field label{display:block;font-size:8.5px;color:var(--label);margin-bottom:2px}
  .field .value{font-size:11px;color:var(--field-text)}
  .cta{width:186px;height:56px;background:var(--cta);color:var(--white);border:0;font-family:"PT Sans",sans-serif;font-size:14px;letter-spacing:.3px;display:flex;align-items:center;justify-content:space-between;padding:0 18px 0 24px}
</style>
</head>
<body>
  <div class="hero-backdrop" role="img" aria-label="Blurred photograph of an airplane wing above the sea at sunset"></div>

  <header class="site-header">
    <div class="brand">Kestrava</div>
    <a class="login-link" href="#">Login/Sign In</a>
  </header>

  <h1 class="headline">Indulge. Infer. Insure.</h1>

  <nav class="product-carousel" aria-label="Insurance types">
    <svg class="carousel-arrow prev" width="14" height="24" viewBox="0 0 14 24"><path d="M12 2 3 12l9 10" fill="none" stroke="rgba(255,255,255,.75)" stroke-width="2.5" stroke-linecap="round"/></svg>

    <div class="product accident">
      <svg width="44" height="30" viewBox="0 0 44 30" fill="none" stroke="rgba(255,255,255,.65)" stroke-width="1.4" stroke-linecap="round" stroke-linejoin="round">
        <path d="M16 10l3-6 2 5 3-7 2 6 4-4-1 6"/>
        <path d="M2 24l6-6 8 2 2 4z"/><circle cx="9" cy="24" r="2"/>
        <path d="M42 24l-6-8-9 3-2 5z"/><circle cx="34" cy="24" r="2"/>
        <path d="M2 27h40"/>
      </svg>
      <span>Accident</span>
    </div>

    <div class="product flight">
      <svg width="84" height="70" viewBox="0 0 84 70" fill="none" stroke="#fff" stroke-width="2.6" stroke-linecap="round" stroke-linejoin="round">
        <path d="M78 6c-3-3-9 0-13 4L56 19 32 12l-5 5 19 12-9 10-8-1-4 4 9 4 4 9 4-4-1-8 10-9 12 19 5-5-7-24 9-9c4-4 7-10 4-13z"/>
        <path d="M22 48 6 64M18 40 8 50M30 56 20 66"/>
      </svg>
      <span>Flight Insurance</span>
    </div>

    <div class="product business">
      <svg width="32" height="28" viewBox="0 0 32 28" fill="none" stroke="rgba(255,255,255,.65)" stroke-width="1.5" stroke-linejoin="round">
        <path d="M4 2h24l3 8H1z"/>
        <path d="M1 10c0 3 5 3 5 0 0 3 5 3 5 0 0 3 5 3 5 0 0 3 5 3 5 0 0 3 5 3 5 0 0 3 5 3 5 0"/>
        <path d="M3 13v13h26V13M8 26v-8h6v8M18 18h7v5h-7z"/>
      </svg>
      <span>Business</span>
    </div>

    <svg class="carousel-arrow next" width="14" height="24" viewBox="0 0 14 24"><path d="M2 2l9 10-9 10" fill="none" stroke="rgba(255,255,255,.75)" stroke-width="2.5" stroke-linecap="round"/></svg>
  </nav>

  <form class="quote-form">
    <div class="field first"><label>First name</label><div class="value">Jméno</div></div>
    <div class="field last"><label>Last name</label><div class="value">Příjmení</div></div>
    <div class="field email"><label>E-mail</label><div class="value">hello@kestrava.com</div></div>
    <button class="cta" type="button">SPOCIAT SENU
      <svg width="14" height="10" viewBox="0 0 14 10" fill="none" stroke="#fff" stroke-width="1.3" stroke-linecap="round"><path d="M1 5h12M9 1l4 4-4 4"/></svg>
    </button>
  </form>
</body>
</html>
```